Law Office Business Card

We need a business card design to include the following information:
Name of Firm: Brennick Law Group, P.A.
Address: 4627 Sandlot Ave, Ste 208, West Palm Beach, FL 33409
Phone: 561-555-0148
Fax: 561-555-0193
Website: http://www.tbrennicklaw.example

We Need a place for the Person's name and email address. Please start with the following:
Lorna K. Dwyer, Esq.
lorna@tbrennicklaw.example

```html
<!DOCTYPE html>
<html lang="en">
<head>
<meta charset="utf-8">
<title>Brennick Law Group – Business Card</title>
<link rel="stylesheet" href="https://fonts.googleapis.com/css2?family=Montserrat:wght@400;500;700&display=swap">
<style>
  :root {
    --backdrop: #ece8e3;
    --card-light: #ffffff;
    --card-dark: #5e5149;
    --accent-tan: #b3a48f;
    --brand-ink: #8a7b6b;
    --text-light: #ffffff;
  }
  * { margin: 0; padding: 0; box-sizing: border-box; }
  html, body {
    width: 1200px; height: 902px; overflow: hidden;
    background: var(--backdrop);
    font-family: "Montserrat", Arial, sans-serif;
  }
  .card {
    position: absolute; left: 120px; top: 178px;
    width: 960px; height: 546px;
    display: flex;
    box-shadow: 0 10px 30px rgba(60, 45, 35, 0.18);
  }
  .card-front {
    width: 476px; height: 100%;
    background: var(--card-light);
    display: flex; flex-direction: column; align-items: center; justify-content: center;
  }
  .divider {
    width: 10px; height: 100%;
    background: linear-gradient(to right, var(--accent-tan) 0 5px, var(--card-light) 5px 10px);
  }
  .card-back {
    flex: 1; height: 100%;
    background: var(--card-dark);
    color: var(--text-light);
    padding: 88px 0 0 50px;
  }
  .brand {
    display: flex; align-items: center; gap: 16px;
  }
  .brand-mark {
    width: 26px; height: 26px;
    border: 2px solid var(--brand-ink);
  }
  .brand-name {
    color: var(--brand-ink);
    font-weight: 500;
    font-size: 30px;
    letter-spacing: 3px;
    text-transform: uppercase;
    line-height: 1.35;
    text-align: center;
  }
  .person-name {
    font-weight: 700; font-size: 30px; letter-spacing: 0.2px;
  }
  .address {
    margin-top: 114px;
    font-size: 24px; line-height: 33px; font-weight: 400;
  }
  .contact-list { list-style: none; margin-top: 14px; }
  .contact-item {
    display: flex; align-items: center; gap: 12px;
    font-size: 24px; height: 35px;
  }
  .contact-icon { width: 26px; height: 26px; flex: none; }
  .website { margin-top: 13px; font-size: 23px; }
</style>
</head>
<body>
  <div class="card">
    <section class="card-front">
      <div class="brand">
        <span class="brand-mark"></span>
        <span class="brand-name">Brennick<br>Law Group</span>
      </div>
    </section>
    <div class="divider"></div>
    <section class="card-back">
      <h1 class="person-name">Lorna K. Dwyer, Esq.</h1>
      <p class="address">4627 Sandlot Ave, Ste 208<br>West Palm Beach, FL 33409</p>
      <ul class="contact-list">
        <li class="contact-item">
          <svg class="contact-icon" viewBox="0 0 26 26" aria-label="Phone">
            <rect width="26" height="26" rx="2" fill="#fff"/>
            <path d="M5 11c0-3 4-5 8-5s8 2 8 5l-3 1-1-2c-2-1-6-1-8 0l-1 2z M8 13h10l2 7H6z" fill="#5e5149"/>
            <circle cx="13" cy="16.5" r="2" fill="#fff"/>
          </svg>
          <span>561-555-0148</span>
        </li>
        <li class="contact-item">
          <svg class="contact-icon" viewBox="0 0 26 26" aria-label="Fax">
            <rect width="26" height="26" rx="2" fill="#fff"/>
            <rect x="8" y="5" width="10" height="6" fill="#5e5149"/>
            <rect x="5" y="10" width="16" height="8" rx="1" fill="#5e5149"/>
            <rect x="8" y="15" width="10" height="6" fill="#5e5149" stroke="#fff" stroke-width="1"/>
          </svg>
          <span>561-555-0193</span>
        </li>
        <li class="contact-item">
          <svg class="contact-icon" viewBox="0 0 26 26" aria-label="Email">
            <rect width="26" height="26" rx="2" fill="#fff"/>
            <rect x="4" y="7" width="18" height="12" fill="none" stroke="#5e5149" stroke-width="1.8"/>
            <path d="M4 7l9 7 9-7M4 19l7-6M22 19l-7-6" fill="none" stroke="#5e5149" stroke-width="1.6"/>
          </svg>
          <span>lorna@tbrennicklaw.example</span>
        </li>
      </ul>
      <p class="website">www.tbrennicklaw.example</p>
    </section>
  </div>
</body>
</html>
```